Website for peer to peer car sharing service

Hi all,

We need a web design for a new environmental friendly peer-to-peer car sharing website.

The website will serve as a marketplace where car owners can list their car and drivers that who do not have access to a car can rent a suitable car. It is important for us to emphasis that this is a community where the main purpose is to use the vehicles on the street in a more efficient way.

Attached are five pictures where we have sketched up the five main pages:

File 1. Info site for a particular car.
File 2. Logo.
File 3. Register a car.
File 4. Sign up.
File 5. Search.
File 6. Front page.

The logo for the company is attached (File 2) and it would be ideal to design the website in relation to the logo. The final design should relate to a secure market place which is environmental friendly.

We would like this webpage to be in the same spirit as www.glimbo.it, www.wavemuse.com, www.powertabventure.com, https://link.hub.org, https://bylane.com etc.

We look forward to see your designs.

Best regards,
The Motiva Team.

Hi guys, 

Please take :

1) Could you please design icons for for  'FAQ' and 'Insurance' in the header, locate the icons right to the Motiva logo. We only want two icons ('FAQ' and 'Insurance')  right to the Motiva logo.

2) The height of the header should be the same as the header of pixora.com

3) The price tags for the cars (below the top section) should be similar to the price tags at wheeldash.com.

4) We would like you to start to design the other pages (the sub-pages listed in the project description:
a)Info site for a particular car.
b)Register a car. 
c)Search results (similar to http://www.zoomfleetly.com/find-car).

Please take a look at the picture attached for the sub-pages:

https://files.examplehost.test/uploads/search_01.jpg

https://files.examplehost.test/uploads/carinfo_02.jpg

http://www.briefbay.test/file.aspx?fileLocation=uploads/register_03.jpg

Best regards, 
Motiva team 

Target Market(s)

The target market are people from 20-40 years old who are environmental friendly, also tourists who visit the city and would like to rent a car.

Industry/Entity Type

It Company

Requirements
Must have
• It is required that the designer that will be chosen will hand in layered PSD files of each web page.

```html
<!DOCTYPE html>
<html lang="en">
<head>
<meta charset="utf-8">
<title>Motiva – Linford Car</title>
<link href="https://fonts.googleapis.com/css2?family=Source+Sans+3:wght@400;600&display=swap" rel="stylesheet">
<style>
:root{
  --green:#5a9a10;
  --green-light:#8cc63f;
  --orange:#f07b18;
  --dark:#323232;
  --tab:#55595c;
  --panel:#eeeeee;
  --row:#efefef;
  --text:#555;
  --muted:#777;
  --footer-text:#b4b4b4;
}
*{margin:0;padding:0;box-sizing:border-box}
html,body{width:1166px;height:1200px;overflow:hidden;background:#fff}
body{font-family:"Source Sans 3",sans-serif;color:var(--text)}
.page{position:relative;width:1166px;height:1200px}
.abs{position:absolute}

.topbar{left:0;top:0;width:1166px;height:33px;background:var(--dark)}
.brand{left:177px;top:4px;color:#fff;font-size:21px;font-weight:600;display:flex;align-items:center;gap:6px}
.brand-dot{width:12px;height:12px;border-radius:50%;background:var(--green-light)}
.top-icon{top:9px}
.nav-link{top:7px;color:#fff;font-size:14px;display:flex;align-items:center;gap:10px}
.dot{width:7px;height:7px;border-radius:50%}

.car-title{left:285px;top:61px;color:var(--green);font-size:16px;font-weight:600}
.tab{left:175px;width:108px;height:29px;background:var(--tab);color:#fff;font-size:13px;padding:6px 0 0 22px}
.tab.active{background:linear-gradient(#7cbc2a,#5a9a10)}

.gallery{left:283px;top:92px;width:420px;height:291px;background:var(--panel)}
.hero{left:4px;top:4px;width:413px;height:219px;background:linear-gradient(180deg,#9fb8cf 0%,#6b8296 45%,#3d4650 75%,#58606a 100%)}
.thumb{top:229px;width:93px;height:55px;border:3px solid #fff}

.section-head{left:290px;color:var(--green);font-size:12.5px;font-weight:600}
.rule{left:285px;width:415px;height:1px;background:#cfcfcf}
.about{left:290px;top:438px;width:410px;font-size:10px;line-height:15px;color:var(--text)}

.stat{left:287px;width:412px;height:28px;background:var(--row);font-size:10.5px}
.stat span{position:absolute;top:8px}
.lbl{color:#555}
.val{color:var(--orange)}
.stars{position:absolute;top:9px}

.review{left:287px;width:412px;height:102px;background:var(--row)}
.review .photo{position:absolute;left:13px;top:10px;width:92px;height:82px}
.review .name{position:absolute;left:123px;top:12px;color:var(--green);font-size:11px}
.review .date{position:absolute;left:123px;top:29px;color:var(--orange);font-size:10.5px;font-style:italic}
.review .body{position:absolute;left:123px;top:46px;width:275px;font-size:8.6px;line-height:15px;color:#666}

.booking{left:740px;top:97px;width:251px;height:265px;background:var(--panel)}
.price-opt{left:757px;font-size:8.5px;color:#666}
.small-head{left:762px;font-size:8.5px;color:var(--green);font-weight:600}
.select{height:22px;background:#fff;border:1px solid #d4d4d4}
.select::after{content:"";position:absolute;right:3px;top:4px;width:12px;height:12px;border:1px solid #888;border-radius:2px;background:#eee}
.select svg{position:absolute;right:5px;top:8px;z-index:1}
.subtotal{left:764px;top:284px;font-size:12.5px;color:#666;font-weight:600}
.subtotal b{color:var(--orange);font-size:15.5px;font-weight:600}
.book-btn{left:764px;top:311px;width:96px;height:33px;background:linear-gradient(#fb9a2a,#ee6c0e);border-radius:2px;color:#fff;font-size:13.5px;text-align:center;line-height:33px}

.owner-head{left:745px;top:379px;color:var(--green);font-size:12.5px;font-weight:600}
.owner{left:740px;top:405px;width:251px;height:286px;background:var(--panel)}
.owner-photo{left:751px;top:417px;width:228px;height:143px;background:linear-gradient(135deg,#f2f2f2,#d9cfc2 55%,#c6b49a);border:1px solid #ddd}
.meta{left:759px;font-size:8.5px;color:#444}
.meta b{color:var(--green);font-weight:400}
.owner-text{left:761px;top:615px;width:225px;font-size:9.8px;line-height:15px;color:#555}

.footer{left:0;top:1048px;width:1166px;height:152px;background:var(--dark)}
.flink{top:1076px;font-size:9.5px;color:var(--footer-text)}
.copy{left:176px;top:1101px;font-size:9.5px;color:var(--footer-text)}
.follow{left:180px;top:1139px;font-size:13px;color:#fff}
.connect{left:180px;top:1166px;font-size:7px;color:var(--footer-text)}
.social{top:1147px;width:26px;height:26px;border-radius:50%;background:#666}
.f-brand{left:620px;top:1067px;font-size:13px;color:#fff}
.contact{left:641px;font-size:9.5px;color:var(--footer-text);line-height:15px}
.c-icon{left:622px}
.f-mark{left:833px;top:1098px;display:flex;align-items:center;gap:8px;color:#4e4e4e;font-size:36px;font-weight:600}
.f-mark i{width:30px;height:30px;border-radius:50%;background:#4e4e4e}
</style>
</head>
<body>
<div class="page">

  <header>
    <div class="abs topbar"></div>
    <div class="abs brand"><span class="brand-dot"></span>Motiva</div>
    <svg class="abs top-icon" style="left:371px" width="19" height="16" viewBox="0 0 19 16" aria-label="FAQ"><path d="M1 1h17v10H8l-4 4v-4H1z" fill="#fff"/><rect x="8.5" y="3" width="2" height="2" fill="#c0311c"/><rect x="8.5" y="6" width="2" height="4" fill="#c0311c"/></svg>
    <svg class="abs top-icon" style="left:409px" width="16" height="14" viewBox="0 0 16 14" aria-label="Shuffle"><path d="M1 4h4l6 6h3M1 10h4l6-6h3" stroke="#fff" stroke-width="1.8" fill="none"/><path d="M12 1l3 3-3 3zM12 7l3 3-3 3z" fill="#fff"/></svg>
    <svg class="abs top-icon" style="left:440px;top:8px" width="19" height="16" viewBox="0 0 19 16" aria-label="Insurance"><path d="M5 12a4 4 0 010-8 5 5 0 019-1 4 4 0 011 9z" fill="#fff"/><path d="M9.5 7v8M7 10l2.5-3 2.5 3" stroke="#323232" stroke-width="1.6" fill="none"/></svg>
    <div class="abs nav-link" style="left:810px"><span class="dot" style="background:#7cbc2a"></span>Sign in</div>
    <div class="abs nav-link" style="left:885px"><span class="dot" style="background:var(--orange)"></span><span style="margin-left:8px">List your Car</span></div>
  </header>

  <h1 class="abs car-title">LINFORD CAR</h1>

  <nav>
    <div class="abs tab active" style="top:96px">PICTURES</div>
    <div class="abs tab" style="top:127px">MAP</div>
    <div class="abs tab" style="top:156px">CALENDER</div>
  </nav>

  <section class="abs gallery">
    <div class="abs hero" role="img" aria-label="Black sports coupe driving across a suspension bridge at dusk"></div>
    <div class="abs thumb" style="left:6px;background:linear-gradient(#9fb2c4,#3a4048)" role="img" aria-label="Black coupe on bridge"></div>
    <div class="abs thumb" style="left:111px;background:linear-gradient(#dfe6ee,#8f9aa4)" role="img" aria-label="Silver sports car"></div>
    <div class="abs thumb" style="left:216px;background:linear-gradient(90deg,#1c3f7a,#b52a1c)" role="img" aria-label="Red car in motion"></div>
    <div class="abs thumb" style="left:320px;background:linear-gradient(#c9d7df,#9a6a3a)" role="img" aria-label="Orange car on a mountain road"></div>
  </section>

  <h2 class="abs section-head" style="top:400px">ABOUT LINFORD CAR</h2>
  <div class="abs rule" style="top:427px"></div>
  <p class="abs about">Lorem Ipsum is simply dummy text of the printing and typesetting industry. Lorem Ipsum has been the industry's standard dummy text ever since the 1500s, when an unknown printer took a galley of type and scrambled it to make a type specimen book. It has survived not only five centuries, but also the leap into electronic typesetting, remaining essentially unchanged...</p>

  <h2 class="abs section-head" style="top:525px">PAGECRAFT STUDIO INCLUDING VERSIONS</h2>
  <div class="abs rule" style="top:552px"></div>

  <svg width="0" height="0" style="position:absolute"><defs><path id="star" d="M5 0l1.5 3.3 3.5.4-2.6 2.4.7 3.5L5 7.8 1.9 9.6l.7-3.5L0 3.7l3.5-.4z"/></defs></svg>

  <div class="abs stat" style="top:562px">
    <span class="lbl" style="left:25px">TRIPS</span><span class="val" style="left:73px">300</span>
    <span class="lbl" style="left:222px">RATING</span><span class="val" style="left:264px">150</span>
  </div>
  <div class="abs stat" style="top:595px">
    <span class="lbl" style="left:25px">RATING</span>
    <svg class="stars" style="left:73px" width="66" height="10"><use href="#star" fill="#f07b18"/><use href="#star" x="14" fill="#f07b18"/><use href="#star" x="28" fill="#f07b18"/><use href="#star" x="42" fill="#aaa"/><use href="#star" x="56" fill="#aaa"/></svg>
    <span class="lbl" style="left:222px">RATING</span>
    <svg class="stars" style="left:265px" width="66" height="10"><use href="#star" fill="#f07b18"/><use href="#star" x="14" fill="#f07b18"/><use href="#star" x="28" fill="#aaa"/><use href="#star" x="42" fill="#aaa"/><use href="#star" x="56" fill="#aaa"/></svg>
  </div>
  <div class="abs stat" style="top:628px">
    <span class="lbl" style="left:25px">RATING</span>
    <svg class="stars" style="left:73px" width="66" height="10"><use href="#star" fill="#f07b18"/><use href="#star" x="14" fill="#f07b18"/><use href="#star" x="28" fill="#f07b18"/><use href="#star" x="42" fill="#aaa"/><use href="#star" x="56" fill="#aaa"/></svg>
    <span class="lbl" style="left:222px">RATING</span>
    <svg class="stars" style="left:265px" width="66" height="10"><use href="#star" fill="#f07b18"/><use href="#star" x="14" fill="#f07b18"/><use href="#star" x="28" fill="#aaa"/><use href="#star" x="42" fill="#aaa"/><use href="#star" x="56" fill="#aaa"/></svg>
  </div>

  <article class="abs review" style="top:679px">
    <div class="photo" style="background:linear-gradient(#e8ecef,#4a4f57)" role="img" aria-label="Reviewer portrait, man in suit"></div>
    <div class="name">DEVON MARSH</div>
    <div class="date">Posted on 27 Jun 2013</div>
    <p class="body">Lorem Ipsum is simply dummy text of the printing and typesetting industry. Lorem Ipsum has been the industry's standard dummy text ever since the 1500s, when an unknown printer...</p>
  </article>
  <article class="abs review" style="top:795px">
    <div class="photo" style="background:linear-gradient(#e3d9b8,#5a8a70)" role="img" aria-label="Reviewer portrait, smiling man outdoors"></div>
    <div class="name">DEVON MARSH</div>
    <div class="date">Posted on 27 Jun 2013</div>
    <p class="body">Lorem Ipsum is simply dummy text of the printing and typesetting industry. Lorem Ipsum has been the industry's standard dummy text ever since the 1500s, when an unknown printer...</p>
  </article>
  <article class="abs review" style="top:912px">
    <div class="photo" style="background:linear-gradient(#eef2f3,#5b6f86)" role="img" aria-label="Reviewer portrait, smiling woman"></div>
    <div class="name">DEVON MARSH</div>
    <div class="date">Posted on 27 Jun 2013</div>
    <p class="body">Lorem Ipsum is simply dummy text of the printing and typesetting industry. Lorem Ipsum has been the industry's standard dummy text ever since the 1500s, when an unknown printer...</p>
  </article>

  <aside>
    <div class="abs booking"></div>
    <div class="abs price-opt" style="top:115px">&raquo;&nbsp; PRICE PER DAY</div>
    <div class="abs price-opt" style="top:132px">&raquo;&nbsp; PRICE PER HOUR</div>
    <div class="abs price-opt" style="top:150px">&raquo;&nbsp; PRICE PER WEEK</div>
    <div class="abs small-head" style="top:178px">START DATE</div>
    <div class="abs select" style="left:761px;top:196px;width:108px"><svg width="8" height="5"><path d="M0 0l4 5 4-5z" fill="#333"/></svg></div>
    <div class="abs select" style="left:878px;top:196px;width:99px"><svg width="8" height="5"><path d="M0 0l4 5 4-5z" fill="#333"/></svg></div>
    <div class="abs small-head" style="top:228px">END DATE</div>
    <div class="abs select" style="left:761px;top:246px;width:108px"><svg width="8" height="5"><path d="M0 0l4 5 4-5z" fill="#333"/></svg></div>
    <div class="abs select" style="left:878px;top:246px;width:99px"><svg width="8" height="5"><path d="M0 0l4 5 4-5z" fill="#333"/></svg></div>
    <div class="abs subtotal">SUB TOTAL <b>$200</b></div>
    <div class="abs book-btn">BOOK IT</div>

    <h2 class="abs owner-head">OWNER INFO</h2>
    <div class="abs owner"></div>
    <div class="abs owner-photo" role="img" aria-label="Car owner portrait, smiling man with glasses"></div>
    <div class="abs meta" style="top:575px">NAME : <b>DEVON MARSH</b></div>
    <div class="abs meta" style="top:592px">LOCATION : <b>NEW JERSY</b></div>
    <p class="abs owner-text">Lorem Ipsum is simply dummy text of the printing and typesetting industry. Lorem Ipsum has been the industry's standard dummy text ever since the 1500s, when an unknown printer...</p>
  </aside>

  <footer>
    <div class="abs footer"></div>
    <div class="abs flink" style="left:176px">Home</div>
    <div class="abs flink" style="left:217px">|</div>
    <div class="abs flink" style="left:237px">About Us</div>
    <div class="abs flink" style="left:290px">|</div>
    <div class="abs flink" style="left:309px">Support</div>
    <div class="abs flink" style="left:357px">|</div>
    <div class="abs flink" style="left:377px">Cars</div>
    <div class="abs flink" style="left:410px">|</div>
    <div class="abs flink" style="left:428px">Insurance</div>
    <div class="abs flink" style="left:484px">|</div>
    <div class="abs flink" style="left:504px">Faq's</div>
    <div class="abs copy">Copyrights © 2013. Motiva. All rights Reserved.</div>
    <div class="abs follow">Follow Us</div>
    <div class="abs connect">CONNECT TO OUR SOCIAL NETWORK :</div>
    <div class="abs social" style="left:346px" aria-label="Social network"></div>
    <div class="abs social" style="left:379px" aria-label="Social network"></div>
    <div class="abs social" style="left:413px" aria-label="Social network"></div>
    <div class="abs social" style="left:446px" aria-label="Social network"></div>
    <div class="abs social" style="left:479px" aria-label="Social network"></div>

    <div class="abs f-brand">Motiva</div>
    <svg class="abs c-icon" style="top:1093px" width="10" height="13" viewBox="0 0 10 13"><path d="M5 0a5 5 0 015 5c0 3-5 8-5 8S0 8 0 5a5 5 0 015-5z" fill="#999"/><circle cx="5" cy="5" r="2" fill="#323232"/></svg>
    <div class="abs contact" style="top:1089px">No 12 Street name,&nbsp; Area,<br>City, Zip Code-1111 111</div>
    <svg class="abs c-icon" style="top:1132px" width="10" height="14" viewBox="0 0 10 14"><rect x="1" y="0.5" width="8" height="13" rx="1.5" fill="none" stroke="#999" stroke-width="1.4"/><rect x="3" y="2.5" width="4" height="7" fill="#999"/></svg>
    <div class="abs contact" style="top:1132px">Call Us : ( 1111 ) 111 111</div>
    <svg class="abs c-icon" style="top:1161px" width="13" height="9" viewBox="0 0 13 9"><rect width="13" height="9" fill="#999"/><path d="M0 0l6.5 5L13 0" stroke="#323232" fill="none"/></svg>
    <div class="abs contact" style="top:1157px">Email Us : motiva@mailbox.test</div>

    <div class="abs f-mark"><i></i>Motiva</div>
  </footer>

</div>
</body>
</html>
```